Website improvements and Adding Functionalities at https://quorin.net/tamberly

1.Search functionality
2.Payment process functionality
3. Application configuration
4. Registration functionality activation
5. Chat functionality
6.Language switching functionality (Portuguese & French)
7.Bespoke interactive modules
8. Automated web scraping and data synchronisation mechanisms
9. News Page
10.Webinar facilities
11. Basic SEO optimisation
12. Speed and performance optimisation
13. Security configuration
14. Google Analytics integration
15. Cross-browser and mobile testing
16. Website deployment and launch support

Target Market(s)

My target markets are companies, investors, suppliers and professionals with an interest in the Mozambican oil and gas sector

Industry/Entity Type

Oil and Gas

Coding

Coded - Design and coding required

Number of Pages Required

1 page

Requirements
Must have
• Improve the existing page at https://quorin.net/tamberly and add the following features to it: 1. Search functionality 2. Payment process functionality 3. Application configuration 4. Activation of registration functionality 5. Chat functionality 6. Language switching functionality (Portuguese & French) 7. Bespoke interactive modules 8. Automated web scraping and data synchronisation mechanisms 9. News Page

```html
<!DOCTYPE html>
<html lang="en">
<head>
<meta charset="utf-8">
<title>Tamberly – Oil & Gas Intelligence for Mozambique</title>
<link href="https://fonts.googleapis.com/css2?family=Inter:wght@300;400;500;600;700;800&display=swap" rel="stylesheet">
<style>
:root{
  --accent:#e84a2a;
  --navy:#1f2a44;
  --footer:#0f2340;
  --text:#222;
  --muted:#777;
  --line:#dedede;
  --soft:#f5f5f5;
  --field:#f4f4f4;
}
*{box-sizing:border-box;margin:0;padding:0}
html,body{width:1200px;height:3646px;overflow:hidden}
body{font-family:'Inter',sans-serif;color:var(--text);background:#fff;position:relative}
.abs{position:absolute}
a{color:inherit;text-decoration:none}

/* header */
.header{position:absolute;left:0;top:0;width:1200px;height:82px;background:#fff}
.brand{position:absolute;left:165px;top:18px;display:flex;align-items:center;gap:8px;font-weight:700;font-size:17px;color:var(--navy)}
.brand i{width:16px;height:16px;border-radius:50%;background:var(--accent);display:block}
.search{position:absolute;left:313px;top:16px;width:328px;height:31px;border:1px solid var(--line);border-radius:6px;font-size:9px;color:#999;padding:9px 12px}
.search svg{position:absolute;right:10px;top:6px}
.lang{position:absolute;left:757px;top:23px;font-size:10px;display:flex;align-items:center;gap:4px}
.btn-login{position:absolute;left:823px;top:16px;width:84px;height:31px;border:1px solid #ccc;border-radius:5px;font-size:9px;text-align:center;line-height:29px}
.btn-register{position:absolute;left:918px;top:16px;width:84px;height:31px;background:var(--accent);color:#fff;border-radius:5px;font-size:9px;text-align:center;line-height:31px}
.cart{position:absolute;left:1012px;top:22px}
.cart b{position:absolute;left:12px;top:-4px;width:9px;height:9px;border-radius:50%;background:var(--accent);font-size:6px;color:#fff;text-align:center;line-height:9px}
.nav{position:absolute;top:64px;font-size:9px;color:#333}
.nav.active{color:var(--accent)}
.nav.active::after{content:"";position:absolute;left:0;right:0;top:14px;height:1px;background:var(--accent)}

/* hero */
.hero{position:absolute;left:0;top:82px;width:1200px;height:538px;background:linear-gradient(100deg,#27353b 0%,#3d4e52 40%,#5a5548 65%,#6b5232 80%,#2c3438 100%)}
.hero-kicker{position:absolute;left:165px;top:224px;font-size:19px;letter-spacing:7px;color:#fff;font-weight:400}
.hero-title{position:absolute;left:163px;top:248px;font-size:52px;font-weight:600;color:#fff;letter-spacing:-.5px}
.hero-title span{color:var(--accent);font-weight:800}
.hero-sub{position:absolute;left:164px;top:313px;font-size:28px;font-weight:300;color:#fff}
.hero-text{position:absolute;left:165px;top:365px;width:500px;font-size:15px;line-height:19px;color:#fff}
.btn-solid{position:absolute;background:var(--accent);color:#fff;font-size:11px;font-weight:600;text-align:center;border-radius:2px}
.btn-ghost{position:absolute;border:1px solid #fff;color:#fff;font-size:11px;font-weight:600;text-align:center;border-radius:2px}
.stats{position:absolute;left:320px;top:553px;width:880px;height:67px;background:rgba(20,32,42,.55);display:flex;align-items:center;padding-left:12px}
.stat{display:flex;align-items:center;gap:8px;color:#fff;width:150px}
.stat strong{display:block;font-size:19px;font-weight:500;line-height:20px}
.stat small{font-size:9px}

/* what */
.frame{position:absolute;left:263px;top:682px;width:207px;height:200px;border:1.5px solid var(--accent);border-radius:18px}
.photo{position:absolute;border-radius:16px}
.h2{font-size:34px;font-weight:400;color:var(--navy)}
.h2 b{font-weight:700}
.lead{position:absolute;left:516px;top:724px;width:460px;font-size:13px;line-height:17px;color:#444}
.feature{position:absolute;width:250px;display:flex;gap:16px}
.feature .ico{width:56px;height:56px;border-radius:50%;background:#f3f3f3;flex:none;display:flex;align-items:center;justify-content:center}
.feature h4{font-size:12px;font-weight:600;color:var(--navy);margin-top:8px}
.feature p{font-size:9px;color:#777;line-height:11px;margin-top:6px;width:175px}

/* opportunities */
.opps{position:absolute;left:0;top:1186px;width:1200px;height:854px;background:var(--soft)}
.center-h{position:absolute;left:0;width:1200px;text-align:center;font-size:35px;font-weight:400;color:var(--navy)}
.center-h b{font-weight:700}
.opp{position:absolute;left:165px;width:870px;height:126px}
.opp .pic{position:absolute;left:0;top:0;width:196px;height:126px;border-radius:14px}
.tag{position:absolute;left:227px;top:23px;font-size:9px;color:#fff;padding:1px 7px;border-radius:2px;letter-spacing:.3px}
.tag.project{background:#2f8a3b}
.tag.tender{background:#e59a10}
.opp h3{position:absolute;left:227px;top:42px;font-size:12px;font-weight:600;color:var(--navy)}
.opp .org{position:absolute;left:227px;top:64px;font-size:9px;color:#777}
.opp .meta{position:absolute;left:227px;top:86px;font-size:9px;color:#555;display:flex;align-items:center;gap:4px}
.opp .meta b{font-weight:600;color:#333}
.btn-detail{position:absolute;left:778px;top:46px;width:92px;height:34px;background:#fff;border:1px solid #ddd;border-radius:3px;font-size:9px;font-weight:600;text-align:center;line-height:32px;color:var(--navy)}

/* news */
.card{position:absolute;top:2177px;width:281px;height:385px;background:#fff;border-radius:14px;box-shadow:0 4px 16px rgba(0,0,0,.07);overflow:hidden}
.card .pic{height:200px}
.card h3{margin:22px 12px 0;font-size:12px;font-weight:600;color:var(--navy);line-height:15px}
.card p{margin:12px 12px 0;font-size:9.5px;line-height:16px;color:#666}
.card .foot{position:absolute;left:12px;right:24px;bottom:30px;display:flex;justify-content:space-between;align-items:center}
.btn-read{width:91px;height:34px;border:1px solid #f0a898;border-radius:3px;color:var(--accent);font-size:9px;text-align:center;line-height:32px}
.date{font-size:12px;color:#555;display:flex;align-items:center;gap:8px}

/* contact */
.contact-h{position:absolute;left:165px;top:2810px;font-size:36px;font-weight:400;color:var(--navy);line-height:41px}
.contact-h b{font-weight:700}
.field{position:absolute;background:var(--field);border:1px solid #e2e2e2;border-radius:3px;font-size:11px;color:#555;padding:13px 11px}

/* footer */
.footer{position:absolute;left:0;top:3328px;width:1200px;height:318px;background:var(--footer);color:#fff}
.footer .brand{top:58px;color:#fff}
.footer .about{position:absolute;left:165px;top:117px;width:210px;font-size:10px;line-height:12px}
.fcol{position:absolute;top:68px}
.fcol h5{font-size:12px;font-weight:500;margin-bottom:14px}
.fcol li{list-style:none;font-size:10px;margin-bottom:10px;color:#dfe3ea}
.fcol .row{display:flex;gap:8px;align-items:center}
.social{position:absolute;top:196px;display:flex;gap:9px;left:165px}
.social span{width:20px;height:20px;border:1.5px solid #fff;border-radius:50%}
.copy{position:absolute;left:0;width:1200px;top:290px;text-align:center;font-size:9px;color:#7f8ba0}
</style>
</head>
<body>

<header class="header">
  <div class="brand"><i></i>Tamberly</div>
  <div class="search">Search companies, tenders, projects, news, training...
    <svg width="18" height="18" viewBox="0 0 18 18" fill="none" stroke="#333" stroke-width="1.3"><circle cx="8" cy="8" r="6"/><path d="M12.5 12.5l4 4"/></svg>
  </div>
  <div class="lang">
    <svg width="16" height="16" viewBox="0 0 16 16" fill="none" stroke="#333" stroke-width="1.1"><circle cx="8" cy="8" r="7"/><ellipse cx="8" cy="8" rx="3" ry="7"/><path d="M1 8h14"/></svg>EN
    <svg width="7" height="5" viewBox="0 0 7 5"><path d="M0 0h7L3.5 5z" fill="#333"/></svg>
  </div>
  <a class="btn-login">Log In</a>
  <a class="btn-register">Register</a>
  <div class="cart">
    <svg width="16" height="15" viewBox="0 0 16 15" fill="none" stroke="#333" stroke-width="1.2"><path d="M1 1h2.5l2 9h8l1.5-6H4.3"/><circle cx="6.5" cy="13" r="1"/><circle cx="12.5" cy="13" r="1"/></svg><b>0</b>
  </div>
  <a class="nav active" style="left:314px">Home</a>
  <a class="nav" style="left:376px">Companies</a>
  <a class="nav" style="left:461px">Projects</a>
  <a class="nav" style="left:534px">Tenders</a>
  <a class="nav" style="left:605px">News</a>
  <a class="nav" style="left:666px">Training</a>
  <a class="nav" style="left:737px">Webinars</a>
  <a class="nav" style="left:814px">Market Data</a>
  <a class="nav" style="left:903px">Suppliers</a>
</header>

<section class="hero" role="img" aria-label="Offshore oil rig platform at sea under a stormy sky"></section>
<div class="hero-kicker">ONE PLATFORM</div>
<h1 class="hero-title">Complete <span>Oil &amp; Gas</span></h1>
<div class="hero-sub">Intelligence for Mozambique</div>
<p class="hero-text">Your trusted platform for market intelligence, opportunities, training, and industry insights.</p>
<a class="btn-solid" style="left:165px;top:435px;width:160px;height:43px;line-height:43px">Explore Opportunities</a>
<a class="btn-ghost" style="left:338px;top:435px;width:162px;height:43px;line-height:41px">Join Tamberly</a>

<div class="stats">
  <div class="stat"><svg width="30" height="30" viewBox="0 0 30 30" fill="none" stroke="#e84a2a" stroke-width="1.5"><rect x="5" y="6" width="20" height="22"/><path d="M10 11h3M17 11h3M10 16h3M17 16h3M10 21h3M17 21h3"/></svg><div><strong>500+</strong><small>Companies</small></div></div>
  <div class="stat"><svg width="30" height="30" viewBox="0 0 30 30" fill="none" stroke="#e84a2a" stroke-width="1.5"><rect x="3" y="9" width="24" height="17" rx="2"/><path d="M11 9V6h8v3M3 16h24"/></svg><div><strong>1,200+</strong><small>Opportunities</small></div></div>
  <div class="stat"><svg width="34" height="30" viewBox="0 0 34 30" fill="none" stroke="#e84a2a" stroke-width="1.5"><path d="M3 28h28M6 28V18h5v10M14 28V12h5v16M22 28V6h5v22"/></svg><div><strong>120+</strong><small>Projects</small></div></div>
  <div class="stat"><svg width="32" height="32" viewBox="0 0 32 32" fill="none" stroke="#e84a2a" stroke-width="1.5"><circle cx="16" cy="16" r="6"/><circle cx="16" cy="16" r="12" stroke-dasharray="4 3"/></svg><div><strong>8,500+</strong><small>Professionals</small></div></div>
  <div class="stat"><svg width="34" height="34" viewBox="0 0 34 34" fill="none" stroke="#e84a2a" stroke-width="1.5"><circle cx="17" cy="17" r="14"/><ellipse cx="17" cy="17" rx="6" ry="14"/><path d="M3 17h28M5 10h24M5 24h24"/></svg><div><strong>Live</strong><small>Market Data</small></div></div>
</div>

<!-- what would you like to do -->
<div class="frame"></div>
<div class="photo" role="img" aria-label="Industrial power plant with red pipelines and chimneys" style="left:165px;top:697px;width:288px;height:411px;background:linear-gradient(180deg,#b9c2cb 0%,#8e8a84 45%,#7a3a36 75%,#5d2a28 100%)"></div>
<h2 class="h2 abs" style="left:516px;top:673px">What Would You <b>Like To Do?</b></h2>
<p class="lead">Explore our energy solutions, request a quote, browse products, or connect with our team for your next project.</p>

<div class="feature" style="left:516px;top:798px"><div class="ico"><svg width="22" height="22" viewBox="0 0 22 22" fill="none" stroke="#e84a2a" stroke-width="1.3"><circle cx="10" cy="10" r="7"/><path d="M15 15l5 5"/></svg></div><div><h4>Search Opportunities</h4><p>Find projects, tenders, companies &amp; more</p></div></div>
<div class="feature" style="left:780px;top:798px"><div class="ico"><svg width="22" height="22" viewBox="0 0 22 22" fill="none" stroke="#e84a2a" stroke-width="1.3"><rect x="2" y="2" width="18" height="18" rx="5"/><path d="M6 14l4-4 3 3 4-5"/></svg></div><div><h4>Market Intelligence</h4><p>Real-time data &amp; industry insights</p></div></div>
<div class="feature" style="left:516px;top:880px"><div class="ico"><svg width="22" height="22" viewBox="0 0 22 22" fill="none" stroke="#e84a2a" stroke-width="1.3"><circle cx="11" cy="7" r="3.5"/><circle cx="4.5" cy="10" r="2.5"/><circle cx="17.5" cy="10" r="2.5"/><path d="M5 19c0-4 3-6 6-6s6 2 6 6"/></svg></div><div><h4>Supplier Directory</h4><p>Connect with verified suppliers</p></div></div>
<div class="feature" style="left:780px;top:880px"><div class="ico"><svg width="22" height="22" viewBox="0 0 22 22" fill="none" stroke="#e84a2a" stroke-width="1.3"><path d="M1 9l10-5 10 5-10 5z"/><path d="M5 11v5c3 3 9 3 12 0v-5"/></svg></div><div><h4>Training &amp; Development</h4><p>Upskill with industry recognized courses</p></div></div>
<div class="feature" style="left:516px;top:960px"><div class="ico"><svg width="22" height="22" viewBox="0 0 22 22" fill="none" stroke="#e84a2a" stroke-width="1.3"><rect x="3" y="4" width="16" height="15" rx="2"/><path d="M3 8h16M7 2v4M15 2v4M7 12h2M11 12h2M15 12h1M7 15h2M11 15h2"/></svg></div><div><h4>Webinars &amp; Events</h4><p>Join live &amp; on-demand industry sessions</p></div></div>
<div class="feature" style="left:516px;top:1041px"><div class="ico"><svg width="22" height="22" viewBox="0 0 22 22" fill="none" stroke="#e84a2a" stroke-width="1.3"><circle cx="11" cy="11" r="3"/><path d="M11 2v3M11 17v3M2 11h3M17 11h3M4.6 4.6l2.1 2.1M15.3 15.3l2.1 2.1M4.6 17.4l2.1-2.1M15.3 6.7l2.1-2.1"/></svg></div><div><h4>Application Configurator</h4><p>Customize your dashboard &amp; alert preferences</p></div></div>
<div class="photo" role="img" aria-label="Field worker in orange safety gear working on a valve" style="left:891px;top:965px;width:144px;height:159px;background:linear-gradient(160deg,#6f8fa6 0%,#c2762e 50%,#3b4a6a 100%)"></div>

<!-- opportunities -->
<section class="opps"></section>
<h2 class="center-h" style="top:1245px">Latest <b>Opportunities</b></h2>

<div class="opp" style="top:1327px">
  <div class="pic" role="img" aria-label="LNG processing plant at dusk" style="background:linear-gradient(180deg,#6d8fc4 0%,#a9a3c0 50%,#4b5a73 100%)"></div>
  <span class="tag project">PROJECT</span>
  <h3>Lúrio LNG Development Area 1</h3>
  <div class="org">Northvane Energy</div>
  <div class="meta"><svg width="12" height="12" viewBox="0 0 12 12" fill="none" stroke="#e84a2a" stroke-width="1"><path d="M6 11s4-3.5 4-6.5a4 4 0 00-8 0C2 7.5 6 11 6 11z"/><circle cx="6" cy="4.5" r="1.4"/></svg>Cabo Delgado | Deadline: <b>30 May 2024</b></div>
  <a class="btn-detail">View Details</a>
</div>
<div class="opp" style="top:1479px">
  <div class="pic" role="img" aria-label="Refinery towers under a blue sky" style="background:linear-gradient(180deg,#8db4d8 0%,#b7bcc2 55%,#5e646b 100%)"></div>
  <span class="tag tender">TENDER</span>
  <h3>Supply of Drilling Equipment &amp; Services</h3>
  <div class="org">Marlow Hydrocarbons</div>
  <div class="meta"><svg width="12" height="12" viewBox="0 0 12 12" fill="none" stroke="#e84a2a" stroke-width="1"><path d="M6 11s4-3.5 4-6.5a4 4 0 00-8 0C2 7.5 6 11 6 11z"/><circle cx="6" cy="4.5" r="1.4"/></svg>Maputo | Deadline: <b>25 May 2024</b></div>
  <a class="btn-detail">View Details</a>
</div>
<div class="opp" style="top:1632px">
  <div class="pic" role="img" aria-label="Offshore platform at sunset over the sea" style="background:linear-gradient(180deg,#5b6fa3 0%,#d98a4e 55%,#2f4360 100%)"></div>
  <span class="tag project">PROJECT</span>
  <h3>Ilha Azul FLNG Project</h3>
  <div class="org">Calvera Petroli</div>
  <div class="meta"><svg width="12" height="12" viewBox="0 0 12 12" fill="none" stroke="#e84a2a" stroke-width="1"><path d="M6 11s4-3.5 4-6.5a4 4 0 00-8 0C2 7.5 6 11 6 11z"/><circle cx="6" cy="4.5" r="1.4"/></svg>Inhambane | Deadline: <b>15 May 2024</b></div>
  <a class="btn-detail">View Details</a>
</div>
<div class="opp" style="top:1784px">
  <div class="pic" role="img" aria-label="Engineer in hard hat at a refinery with flare" style="background:linear-gradient(120deg,#4d6688 0%,#d27a3a 50%,#8a2a24 100%)"></div>
  <span class="tag tender">TENDER</span>
  <h3>Maintenance Services for Onshore Facilities</h3>
  <div class="org">Oduya Chemicals</div>
  <div class="meta"><svg width="12" height="12" viewBox="0 0 12 12" fill="none" stroke="#e84a2a" stroke-width="1"><path d="M6 11s4-3.5 4-6.5a4 4 0 00-8 0C2 7.5 6 11 6 11z"/><circle cx="6" cy="4.5" r="1.4"/></svg>Temane | Deadline: <b>5 May 2024</b></div>
  <a class="btn-detail">View Details</a>
</div>
<a class="btn-solid" style="left:519px;top:1934px;width:162px;height:44px;line-height:44px">View More</a>

<!-- news -->
<h2 class="center-h" style="top:2095px">Industry <b>News</b></h2>
<article class="card" style="left:165px">
  <div class="pic" role="img" aria-label="Gas processing site with flare stack" style="background:linear-gradient(180deg,#9fb2c4 0%,#8b8272 60%,#5e4c3a 100%)"></div>
  <h3>Mozambique Aims to Boost Natural Gas Production by 2025</h3>
  <p>There are many variations of passages of Lorem Ipsum available, but the majority have suffered alteration in some form, by injected humour</p>
  <div class="foot"><a class="btn-read">Read More</a><span class="date"><svg width="13" height="13" viewBox="0 0 13 13" fill="none" stroke="#555"><rect x="1" y="2" width="11" height="10" rx="1"/><path d="M1 5h11M4 1v2M9 1v2"/></svg>May 10, 2024</span></div>
</article>
<article class="card" style="left:460px">
  <div class="pic" role="img" aria-label="Industrial storage silos under a bright sky" style="background:linear-gradient(180deg,#7fa8d6 0%,#c7ccd1 55%,#6e7378 100%)"></div>
  <h3>Calvera Announces New Drilling Campaign Offshore Mozambique</h3>
  <p>There are many variations of passages of Lorem Ipsum available, but the majority have suffered alteration in some form, by injected humour</p>
  <div class="foot"><a class="btn-read">Read More</a><span class="date"><svg width="13" height="13" viewBox="0 0 13 13" fill="none" stroke="#555"><rect x="1" y="2" width="11" height="10" rx="1"/><path d="M1 5h11M4 1v2M9 1v2"/></svg>May 8, 2024</span></div>
</article>
<article class="card" style="left:754px">
  <div class="pic" role="img" aria-label="Offshore drilling rig silhouetted at sunset" style="background:linear-gradient(180deg,#3e5f8f 0%,#e39a3c 55%,#2b3a52 100%)"></div>
  <h3>Local Content Development Key Focus for Oil &amp; Gas Growth</h3>
  <p>There are many variations of passages of Lorem Ipsum available, but the majority have suffered alteration in some form, by injected humour</p>
  <div class="foot"><a class="btn-read">Read More</a><span class="date"><svg width="13" height="13" viewBox="0 0 13 13" fill="none" stroke="#555"><rect x="1" y="2" width="11" height="10" rx="1"/><path d="M1 5h11M4 1v2M9 1v2"/></svg>May 6, 2024</span></div>
</article>
<a class="btn-solid" style="left:519px;top:2604px;width:162px;height:44px;line-height:44px">View More</a>

<!-- contact -->
<h2 class="contact-h">Ready To Explore<br><b>A Trade?</b></h2>
<div class="field" style="left:165px;top:2918px;width:232px;height:43px">First Name*</div>
<div class="field" style="left:410px;top:2918px;width:232px;height:43px">Last Name*</div>
<div class="field" style="left:165px;top:2978px;width:232px;height:43px">Email*</div>
<div class="field" style="left:410px;top:2978px;width:232px;height:43px">Phone*</div>
<div class="field" style="left:165px;top:3036px;width:477px;height:122px">Message</div>
<a class="btn-solid" style="left:165px;top:3184px;width:477px;height:43px;line-height:43px;border-radius:3px">Get In Touch</a>
<div class="photo" role="img" aria-label="Refinery towers lit up at sunset" style="left:672px;top:2772px;width:363px;height:493px;border-radius:22px;background:linear-gradient(180deg,#3d5c95 0%,#c96a45 35%,#f0a03a 55%,#3a3a44 80%,#1f2533 100%)"></div>

<!-- footer -->
<footer class="footer">
  <div class="brand"><i></i>Tamberly</div>
  <p class="about">Reliable skip hire and waste management services for homes, businesses and construction projects.</p>
  <div class="social"><span></span><span></span><span></span></div>
  <div class="fcol" style="left:435px"><h5>Quick Links</h5><ul><li>Companies</li><li>Projects</li><li>Tenders</li><li>Market Data</li><li>Suppliers</li></ul></div>
  <div class="fcol" style="left:617px"><h5>Information</h5><ul><li>Waste Types</li><li>Environmental Policy</li><li>Terms &amp; Conditions</li><li>Privacy Policy</li><li>Sitemap</li></ul></div>
  <div class="fcol" style="left:822px"><h5>Contact Us</h5><ul>
    <li class="row"><svg width="11" height="11" viewBox="0 0 11 11"><path d="M2 1l2 0 1 2.5-1.3 1a6 6 0 002.8 2.8l1-1.3L10 7v2a1 1 0 01-1 1A9 9 0 011 2a1 1 0 011-1z" fill="#e84a2a"/></svg>0800 123 4567</li>
    <li class="row"><svg width="11" height="9" viewBox="0 0 11 9"><rect width="11" height="9" rx="1" fill="#e84a2a"/><path d="M1 1l4.5 4L10 1" stroke="#fff" fill="none"/></svg>info@yourdomain.co.uk</li>
    <li class="row"><svg width="11" height="11" viewBox="0 0 11 11"><rect x="0" y="1" width="11" height="10" rx="1" fill="#e84a2a"/><path d="M0 4h11" stroke="#fff"/></svg>Mon – Fri 7am – 7pm &nbsp;&nbsp;&nbsp; Sat 7am – 1pm</li>
    <li class="row"><svg width="10" height="12" viewBox="0 0 10 12"><path d="M5 12S0 7.5 0 4.5a5 5 0 0110 0C10 7.5 5 12 5 12z" fill="#e84a2a"/><circle cx="5" cy="4.5" r="1.6" fill="#fff"/></svg>123 Recycling Way, Yourtown, YT1 2AB</li>
  </ul></div>
  <div class="copy">© 2026 by Tamberly Co. All Rights Reserved.</div>
</footer>

</body>
</html>
```